National Mission Critical Construction Contractor needs Stationery Design to make a bold statement

We are a small commercial construction company, working primarily in mission critical facilities across the U.S.. We have exciting corporate changes going an and a new logo and office space so we need new stationery. The final design should incorporate our new logo and invoke a fresh, high-tech feel while looking simple and modern.

Industry/Entity Type

Construction

Contact Information for Business Card

We are required to list our state licensing qualifications on the back of our card.

Font styles to use
Sans Serif

Requirements
Must have
• We need to have a design for second page of stationery, envelopes both standard and with a window and for a 3 x 4 notepad.

```html
<!DOCTYPE html>
<html lang="en">
<head>
<meta charset="utf-8">
<title>Northgate Construction Management – Stationery</title>
<link rel="stylesheet" href="https://fonts.googleapis.com/css2?family=Questrial&display=swap">
<style>
  :root {
    --brand-blue: #0c72b9;
    --brand-green: #8cc540;
    --paper: #ffffff;
    --backdrop: #d6d8da;
    --watermark: #e6ecf6;
  }
  * { box-sizing: border-box; margin: 0; padding: 0; }
  html, body { width: 1200px; height: 927px; overflow: hidden; }
  body {
    background: var(--backdrop);
    font-family: "Questrial", Arial, sans-serif;
    position: relative;
  }
  .piece { position: absolute; overflow: hidden; }

  /* wordmark */
  .wordmark { display: flex; align-items: center; gap: 10px; }
  .wordmark-dot { border-radius: 50%; border: 3px solid currentColor; flex: none; }
  .wordmark-text { display: flex; flex-direction: column; line-height: 1; }
  .wordmark-name { letter-spacing: 0.5px; }
  .wordmark-tag { letter-spacing: 2px; }

  /* letterhead */
  .letterhead { left: 149px; top: 50px; width: 439px; height: 566px; background: var(--paper); }
  .letterhead-band { position: absolute; left: 0; top: 0; width: 100%; height: 42px; background: var(--brand-blue); }
  .letterhead-label {
    position: absolute; left: 126px; top: 0; width: 188px; height: 42px; background: var(--paper);
    color: var(--brand-blue); display: flex; flex-direction: column; align-items: center; justify-content: center; gap: 5px;
  }
  .letterhead-label .wordmark-name { font-size: 19px; }
  .letterhead-label .wordmark-tag { font-size: 7px; letter-spacing: 1.4px; border-top: 1px solid #b7c6d8; padding-top: 3px; }
  .letterhead-accent { position: absolute; left: 126px; top: 42px; width: 188px; height: 42px; background: var(--brand-green); }
  .letterhead-watermark {
    position: absolute; left: 113px; top: 222px; width: 212px; height: 212px;
    border-radius: 50%; border: 4px solid var(--watermark);
  }
  .letterhead-rule { position: absolute; left: 19px; top: 512px; width: 400px; height: 1px; background: var(--brand-blue); }
  .contact-list { position: absolute; left: 19px; top: 519px; list-style: none; color: var(--brand-blue); font-size: 9.6px; line-height: 12px; }
  .contact-list li { display: flex; align-items: center; gap: 6px; }
  .contact-list svg { width: 7px; height: 7px; }
  .contact-list b, .url b { font-weight: 700; }
  .letterhead-address { position: absolute; right: 20px; top: 531px; text-align: right; color: var(--brand-blue); font-size: 9.6px; line-height: 12px; }

  /* folder */
  .folder { left: 611px; top: 50px; width: 439px; height: 566px; background: var(--brand-blue); }
  .folder .wordmark { position: absolute; left: 66px; top: 245px; color: var(--paper); }
  .folder .wordmark-dot { width: 74px; height: 74px; }
  .folder .wordmark-name { font-size: 30px; border-bottom: 2px solid var(--paper); padding-bottom: 3px; }
  .folder .wordmark-tag { font-size: 9.5px; margin-top: 7px; }
  .folder-base { position: absolute; left: 0; top: 524px; width: 100%; height: 42px; background: var(--paper); }
  .folder-accent { position: absolute; left: 126px; top: 482px; width: 188px; height: 42px; background: var(--brand-green); }
  .folder-url {
    position: absolute; left: 126px; top: 524px; width: 188px; height: 42px; background: var(--brand-blue);
    color: var(--paper); font-size: 15.5px; display: flex; align-items: center; justify-content: center;
  }

  /* envelope front */
  .envelope-front { left: 135px; top: 644px; width: 454px; height: 234px; background: var(--paper); }
  .envelope-front-flap { position: absolute; left: 0; top: 0; width: 100%; height: 30px; background: var(--brand-blue); border-radius: 16px 16px 0 0; }
  .envelope-front .wordmark { position: absolute; left: 106px; top: 100px; color: var(--brand-blue); }
  .envelope-front .wordmark-dot { width: 58px; height: 58px; }
  .envelope-front .wordmark-name { font-size: 23px; border-bottom: 2px solid #b7c6d8; padding-bottom: 2px; }
  .envelope-front .wordmark-tag { font-size: 7.6px; margin-top: 5px; }
  .envelope-front-address { position: absolute; left: 0; width: 100%; top: 212px; text-align: center; color: var(--brand-blue); font-size: 9.6px; }

  /* envelope back */
  .envelope-back { left: 610px; top: 671px; width: 454px; height: 206px; background: var(--brand-blue); }
  .envelope-back-flap { position: absolute; left: 0; top: 0; width: 100%; height: 30px; background: var(--brand-green); border-radius: 0 0 16px 0; }
  .envelope-back-mark {
    position: absolute; left: 183px; top: 73px; width: 88px; height: 88px; border-radius: 50%;
    border: 3px solid var(--paper);
  }
  .envelope-back-url { position: absolute; left: 0; width: 100%; top: 182px; text-align: center; color: var(--paper); font-size: 11px; }
</style>
</head>
<body>

<section class="piece letterhead" aria-label="Letterhead">
  <div class="letterhead-band"></div>
  <div class="letterhead-label">
    <span class="wordmark-name">NORTHGATE</span>
    <span class="wordmark-tag">CONSTRUCTION MANAGEMENT</span>
  </div>
  <div class="letterhead-accent"></div>
  <div class="letterhead-watermark"></div>
  <div class="letterhead-rule"></div>
  <ul class="contact-list">
    <li><svg viewBox="0 0 10 10"><path d="M2 1l2 2-1 1.5a6 6 0 0 0 2.5 2.5L7 6l2 2-1.5 1.5C4 9 1 6 .5 2.5z" fill="#8cc540"/></svg>+1.555.010.2040</li>
    <li><svg viewBox="0 0 10 10"><rect x="0.5" y="2" width="9" height="6" fill="none" stroke="#8cc540"/><path d="M.5 2l4.5 3.5L9.5 2" fill="none" stroke="#8cc540"/></svg>dana@northgatecm.com</li>
    <li><svg viewBox="0 0 10 10"><circle cx="5" cy="5" r="4.5" fill="#8cc540"/></svg>www.<b>northgatecm</b>.com</li>
  </ul>
  <p class="letterhead-address">48B W. Harbor Ln.<br>Millbrook, TX. 75000</p>
</section>

<section class="piece folder" aria-label="Presentation folder">
  <div class="wordmark">
    <span class="wordmark-dot"></span>
    <span class="wordmark-text">
      <span class="wordmark-name">NORTHGATE</span>
      <span class="wordmark-tag">CONSTRUCTION MANAGEMENT</span>
    </span>
  </div>
  <div class="folder-base"></div>
  <div class="folder-accent"></div>
  <div class="folder-url url">www.<b>northgatecm</b>.com</div>
</section>

<section class="piece envelope-front" aria-label="Envelope front">
  <div class="envelope-front-flap"></div>
  <div class="wordmark">
    <span class="wordmark-dot"></span>
    <span class="wordmark-text">
      <span class="wordmark-name">NORTHGATE</span>
      <span class="wordmark-tag">CONSTRUCTION MANAGEMENT</span>
    </span>
  </div>
  <p class="envelope-front-address">48B W. Harbor Ln. Millbrook, TX. 75000</p>
</section>

<section class="piece envelope-back" aria-label="Envelope back">
  <div class="envelope-back-flap"></div>
  <div class="envelope-back-mark"></div>
  <p class="envelope-back-url url">www.<b>northgatecm</b>.com</p>
</section>

</body>
</html>
```